Modern Business Card Design Needed for Young Realtor

Information that is going on the card:Marcus Penhall
Broker/Owner
555.013.2967
Marcus@MPenhallHomes.example
www.MPenhallHomes.example

Would also like to include my Instagram Handle somewhere. Probably on the back: the_queencity_realtorMy previous business card is attached, I like that one but would like an updated version and maybe a few design changes

Marcus Penhall
Broker/Owner
555.013.2967
Marcus@MPenhallHomes.example
www.MPenhallHomes.example

• Would also like to include my Instagram Handle somewhere. Probably on the back: the_harborline_agent
• Brantley Osgood or the BO (logo from the previous card.)

```html
<!DOCTYPE html>
<html lang="en">
<head>
<meta charset="utf-8">
<title>Marcus Penhall – Business Card</title>
<link rel="stylesheet" href="https://fonts.googleapis.com/css2?family=Lato:wght@400;700;900&family=Questrial&display=swap">
<style>
  :root {
    --page-bg: #ececec;
    --card-dark: #262626;
    --card-light: #ffffff;
    --brand-red: #a51f2e;
    --ink: #2b2b2b;
    --photo-a: #9a9a9a;
    --photo-b: #d8d8d8;
  }
  * { box-sizing: border-box; margin: 0; padding: 0; }
  html, body { width: 1200px; height: 757px; overflow: hidden; }
  body { background: var(--page-bg); position: relative; font-family: "Questrial", sans-serif; }

  .card { position: absolute; overflow: hidden; }

  /* Front */
  .card-front { left: 69px; top: 186px; width: 531px; height: 318px; background: var(--card-light); }
  .front-dark { position: absolute; left: 0; top: 0; width: 100%; height: 212px; background: var(--card-dark); }
  .front-skyline { position: absolute; left: 0; top: 196px; width: 100%; height: 24px;
    background: linear-gradient(var(--card-dark), var(--card-light)); }
  .agent-name { position: absolute; left: 6px; width: 260px; top: 99px; text-align: center;
    white-space: nowrap; line-height: 1;
    font-family: "Lato", sans-serif; font-weight: 900; font-size: 27px; color: #fff; letter-spacing: -0.3px; }
  .agent-title { position: absolute; left: 6px; width: 260px; top: 129px; text-align: center;
    white-space: nowrap; line-height: 1.1;
    font-size: 16px; color: #fff; }
  .agent-photo { position: absolute; left: 257px; top: 33px; width: 250px; height: 250px; border-radius: 50%;
    border: 5px solid #fff; box-shadow: 0 0 0 1px #cfcfcf;
    background: radial-gradient(circle at 50% 40%, var(--photo-b), var(--photo-a)); }
  .front-brand { position: absolute; left: 20px; top: 272px; width: 262px; text-align: center;
    white-space: nowrap; line-height: 1;
    font-size: 22px; letter-spacing: 3px; color: var(--ink); }

  /* Back */
  .card-back { left: 650px; top: 195px; width: 499px; height: 300px; background: var(--card-light); }
  .back-brand { position: absolute; left: 0; top: 68px; width: 100%; text-align: center;
    white-space: nowrap; line-height: 1;
    font-size: 25px; letter-spacing: 3px; color: var(--brand-red); }
  .back-skyline { position: absolute; left: 0; top: 158px; width: 100%; height: 22px;
    background: linear-gradient(var(--card-light), var(--brand-red)); }
  .back-band { position: absolute; left: 0; top: 180px; width: 100%; height: 120px; background: var(--brand-red); }
  .contact { position: absolute; display: flex; align-items: center; gap: 8px; color: #fff; font-size: 13px;
    white-space: nowrap; }
  .contact svg { width: 11px; height: 13px; flex: none; }
  .contact-phone { left: 27px; top: 205px; }
  .contact-email { left: 27px; top: 226px; }
  .contact-web { left: 27px; top: 245px; font-family: "Lato", sans-serif; font-weight: 700; font-size: 13px; }
  .contact-social { left: 327px; top: 226px; }
  .social-dot { width: 19px; height: 19px; border-radius: 50%; background: #fff; flex: none; }
  .disclaimer { position: absolute; left: 27px; top: 276px; font-size: 9.5px; color: #fff; white-space: nowrap; }
</style>
</head>
<body>
  <section class="card card-front">
    <div class="front-dark"></div>
    <div class="front-skyline" role="img" aria-label="City skyline silhouette"></div>
    <h1 class="agent-name">MARCUS PENHALL</h1>
    <p class="agent-title">Broker/Owner</p>
    <div class="agent-photo" role="img" aria-label="Portrait photo of the broker"></div>
    <p class="front-brand">PENHALL HOMES</p>
  </section>

  <section class="card card-back">
    <p class="back-brand">PENHALL HOMES</p>
    <div class="back-skyline" role="img" aria-label="City skyline silhouette"></div>
    <div class="back-band"></div>
    <p class="contact contact-phone">
      <svg viewBox="0 0 11 13"><rect x="2" y="0.5" width="7" height="12" rx="1.2" fill="none" stroke="#fff"/><circle cx="5.5" cy="10.5" r="0.7" fill="#fff"/></svg>
      555.013.2967
    </p>
    <p class="contact contact-email">
      <svg viewBox="0 0 11 13"><rect x="0.5" y="3.5" width="10" height="7" fill="#fff"/><path d="M0.5 3.5 L5.5 7.5 L10.5 3.5" fill="none" stroke="#a51f2e"/></svg>
      Marcus@MPenhallHomes.example
    </p>
    <p class="contact contact-web">www.MPenhallHomes.example</p>
    <p class="contact contact-social"><span class="social-dot"></span>the_harborline_agent</p>
    <p class="disclaimer">*Each Office is Independently Owned &amp; Operated</p>
  </section>
</body>
</html>
```